Tidemark Book Cover for a new author entering the writing space

Design a stunning, eye catching book cover for a Christian Book. Front, back & spine needs to be designed. I am currently reviewing the final draft so the cover will need to be finalized for print once I have the number of pages and the back cover information.

Book Title: Tidemark
Book Subtitle: Walking steady through the longest season.

Author Name: Dr. Colm Basset

Target Market(s)

Christian readers

Industry/Entity Type

Christian

Colors

Designer to choose colors to be used in the design.

Requirements
Must have
• Bold Title
• Bold Author
• Bold color
• Clean design
Should not have
• No angel wings
• No hands coming out of heaven
• No doves

```html
<!DOCTYPE html>
<html lang="en">
<head>
<meta charset="utf-8">
<title>Tidemark — Dr. Colm Basset</title>
<link rel="stylesheet" href="https://fonts.googleapis.com/css2?family=Cinzel:wght@400;600&family=Oswald:wght@700&display=swap">
<style>
  :root {
    --parchment: #efe9dd;
    --parchment-edge: #d9d0c0;
    --title-rust: #a3361b;
    --subtitle-olive: #4c5446;
    --author-ink: #1c1b1a;
    --art-teal: #3f8a86;
    --art-amber: #f0b24a;
    --art-ember: #c4561e;
    --art-shadow: #4a2e1c;
  }
  html, body {
    margin: 0;
    padding: 0;
    width: 807px;
    height: 1200px;
    overflow: hidden;
    background: var(--parchment);
  }
  .cover {
    position: relative;
    width: 807px;
    height: 1200px;
    overflow: hidden;
    background: radial-gradient(ellipse at 50% 40%, #f6f2ea 0%, var(--parchment) 55%, var(--parchment-edge) 100%);
  }
  .cover-title {
    position: absolute;
    top: 80px;
    left: 0;
    width: 100%;
    margin: 0;
    text-align: center;
    font-family: "Cinzel", serif;
    font-weight: 400;
    font-size: 140px;
    line-height: 1.1;
    letter-spacing: 0;
    color: var(--title-rust);
    white-space: nowrap;
  }
  .cover-subtitle {
    position: absolute;
    top: 250px;
    left: 0;
    width: 100%;
    margin: 0;
    text-align: center;
    font-family: "Cinzel", serif;
    color: var(--subtitle-olive);
    white-space: nowrap;
  }
  .cover-subtitle .line-lead {
    display: block;
    font-size: 30px;
    font-weight: 400;
    letter-spacing: 1px;
    line-height: 36px;
  }
  .cover-subtitle .line-key {
    display: block;
    margin-top: 9px;
    font-size: 44px;
    font-weight: 600;
    letter-spacing: 1px;
    line-height: 48px;
  }
  .cover-art {
    position: absolute;
    left: 0;
    top: 380px;
    width: 807px;
    height: 820px;
  }
  .cover-author {
    position: absolute;
    top: 1078px;
    left: 0;
    width: 100%;
    margin: 0;
    text-align: center;
    font-family: "Oswald", sans-serif;
    font-weight: 700;
    font-size: 76px;
    line-height: 1;
    letter-spacing: 10px;
    color: var(--author-ink);
    white-space: nowrap;
  }
</style>
</head>
<body>
<main class="cover">
  <h1 class="cover-title">TIDEMARK</h1>
  <p class="cover-subtitle">
    <span class="line-lead">WALKING STEADY THROUGH THE LONGEST</span>
    <span class="line-key">SEASON.</span>
  </p>

  <svg class="cover-art" viewBox="0 0 807 820" role="img" aria-label="Double-exposure artwork: a man's head in profile filled with a sunlit hillside, trees, a lone figure and faint handwritten script">
    <defs>
      <radialGradient id="art-glow" cx="48%" cy="62%" r="60%">
        <stop offset="0%" stop-color="var(--art-amber)"/>
        <stop offset="50%" stop-color="var(--art-ember)"/>
        <stop offset="100%" stop-color="var(--art-shadow)"/>
      </radialGradient>
      <linearGradient id="art-sky" x1="0" y1="0" x2="0.8" y2="0.7">
        <stop offset="0%" stop-color="var(--art-teal)" stop-opacity="0.9"/>
        <stop offset="45%" stop-color="var(--art-teal)" stop-opacity="0"/>
      </linearGradient>
      <linearGradient id="art-fade" x1="0" y1="0" x2="0" y2="1">
        <stop offset="0%" stop-color="#fff"/>
        <stop offset="78%" stop-color="#fff"/>
        <stop offset="100%" stop-color="#fff" stop-opacity="0.55"/>
      </linearGradient>
      <mask id="art-mask">
        <rect width="807" height="820" fill="url(#art-fade)"/>
      </mask>
      <clipPath id="art-shape">
        <path d="M50 820 C30 560 40 320 120 190 C210 50 400 0 540 60 C660 110 730 260 740 420 C748 560 710 700 650 820 Z"/>
      </clipPath>
    </defs>
    <g clip-path="url(#art-shape)" mask="url(#art-mask)">
      <rect width="807" height="820" fill="url(#art-glow)"/>
      <rect width="807" height="820" fill="url(#art-sky)"/>
    </g>
  </svg>

  <p class="cover-author">DR. COLM BASSET</p>
</main>
</body>
</html>
```